Business card design for engineering firm specializing in defense industry.

We need a professional business card design. Something simple but stands out. We are an engineering company specializing in composites in the defense industry.
Industry/Entity Type
Defense
Contact Information for Business Card
A simple black business card with the Varlonix yellow color is what we had in mind but open for other designs.
Colors
ffc214

```html
<!DOCTYPE html>
<html lang="en">
<head>
<meta charset="utf-8">
<title>Varlonix Business Card</title>
<link href="https://fonts.googleapis.com/css2?family=Roboto:wght@400;700;900&display=swap" rel="stylesheet">
<style>
  :root {
    --backdrop: #d9d9d6;
    --card: #1c1c1c;
    --card-edge: #262626;
    --brand-yellow: #ffc214;
    --ink-light: #ececec;
  }
  * { margin: 0; padding: 0; box-sizing: border-box; }
  html, body {
    width: 1200px; height: 801px; overflow: hidden;
    background: var(--backdrop);
    font-family: "Roboto", Arial, sans-serif;
  }
  .sheet {
    position: relative; width: 1200px; height: 801px;
    display: flex; align-items: center; justify-content: center; gap: 60px;
  }
  .card {
    width: 500px; height: 286px;
    background: linear-gradient(135deg, var(--card-edge), var(--card));
    box-shadow: 0 10px 26px rgba(0,0,0,0.22);
    position: relative;
  }
  .card-front {
    display: flex; align-items: center; justify-content: center; gap: 22px;
  }
  .identity { text-align: right; }
  .identity-name {
    color: var(--brand-yellow); font-weight: 700; font-size: 31px; line-height: 1.05;
  }
  .identity-role {
    color: var(--ink-light); font-size: 15px; margin-top: 4px;
  }
  .divider {
    width: 2px; height: 64px; background: var(--brand-yellow);
  }
  .contacts { list-style: none; }
  .contact-item {
    display: flex; align-items: center; gap: 8px;
    color: var(--ink-light); font-size: 14px; line-height: 1.6;
  }
  .contact-icon { width: 12px; height: 12px; flex: none; }
  .card-back {
    display: flex; align-items: center; justify-content: center;
  }
  .wordmark {
    display: flex; align-items: center; gap: 14px;
  }
  .wordmark-square {
    width: 30px; height: 30px; background: var(--brand-yellow);
  }
  .wordmark-name {
    color: var(--ink-light); font-weight: 900; font-size: 52px; letter-spacing: 0.5px;
  }
</style>
</head>
<body>
<main class="sheet">
  <section class="card card-front" aria-label="Business card front">
    <div class="identity">
      <p class="identity-name">Daniel Hart</p>
      <p class="identity-role">Director</p>
    </div>
    <div class="divider"></div>
    <ul class="contacts">
      <li class="contact-item">
        <svg class="contact-icon" viewBox="0 0 12 12"><path d="M2.5 1 L4.5 1 L5.2 3.6 L4 4.6 Q5 7 7.4 8 L8.4 6.8 L11 7.5 L11 9.5 Q10.5 11 9 11 Q1 10 1 3 Q1 1.5 2.5 1 Z" fill="var(--brand-yellow)"/></svg>
        555 201 4870
      </li>
      <li class="contact-item">
        <svg class="contact-icon" viewBox="0 0 12 12"><rect x="0.5" y="2" width="11" height="8" fill="var(--brand-yellow)"/><path d="M0.5 2 L6 6.5 L11.5 2" stroke="var(--card)" stroke-width="1" fill="none"/></svg>
        info@varlonix.com
      </li>
      <li class="contact-item">
        <svg class="contact-icon" viewBox="0 0 12 12"><circle cx="6" cy="6" r="5.5" fill="var(--brand-yellow)"/><path d="M0.5 6 H11.5 M6 0.5 V11.5 M1.5 3.5 H10.5 M1.5 8.5 H10.5" stroke="var(--card)" stroke-width="0.8"/></svg>
        www.varlonix.com
      </li>
    </ul>
  </section>

  <section class="card card-back" aria-label="Business card back">
    <div class="wordmark">
      <span class="wordmark-square"></span>
      <span class="wordmark-name">Varlonix</span>
    </div>
  </section>
</main>
</body>
</html>
```